Mirelo Japanese Restaurant

We just want the japanese sakura background and the menu as below

Side dish :
Edamame $4
Japanese Steam Green Bean
Crab Craw $3 each
With Japanese mayo
Teriyaki Chicken stick $3 each
Chicken stick with home made teriyaki sauce
Tempura Prawns $7
With Japanese mayo
Miso Soup $3
Traditional Japanese soup
Salt and Pepper Calamari $7
With japanese mayo

Main dish:
Gyu Don $12
Bowl of steam rice topped with beef and onion simmered in a mildly sweet sauce.
Teriyaki Don $12
Bowl of steam rice topped with your choice of beef, chicken or pork and with our special Teriyaki sauce.
Vege Don $12
Bowl of steam rice with seasonal Vegetables with the special japanese sweet soy sauce.
Japanese Curry $12,(prawns $14)
Bowl of steam rice with Chicken, pork or prawn with japanese mild curry sauce.
Katsu Don $12
Bowl of steam rice topped with a deep-fried pork cutlet and egg with the japanese special sauce.
Oyako Don $12
Bowl of steam rice topped with chick and egg with japanese special sauce.
Spice Don $12
Bowl of steam rice topped with beef or chicken with japanese spice sauce.
Gingle Don $12
Bowl of steam rice topped with beef or chicken with japanese ginger sauce.
Sushi $3
Roll everyday on seasonal
ingredient.

Japanese-style sweets
Black Sesame Ice cream $4.5
Green tea Ice cream $4.5

Restaurant

```html
<!DOCTYPE html>
<html lang="en">
<head>
<meta charset="utf-8">
<title>Mirelo Japanese Restaurant – Menu</title>
<link rel="stylesheet" href="https://fonts.googleapis.com/css2?family=Kaushan+Script&family=Caveat:wght@500&family=Fira+Sans:ital,wght@0,600;1,400&display=swap">
<style>
  :root {
    --backdrop: #0b0b0b;
    --red-deep: #7a0a0c;
    --red: #c4161c;
    --red-bright: #e02a26;
    --blossom: #9e2a34;
    --band: #141010;
    --gold: #e8c21d;
    --panel-yellow: #f2d418;
    --panel-cream: #fffef6;
    --ink: #1a1a1a;
  }
  * { box-sizing: border-box; margin: 0; padding: 0; }
  html, body { width: 1200px; height: 1000px; overflow: hidden; }
  body {
    background: var(--backdrop);
    font-family: "Fira Sans", Arial, sans-serif;
    color: var(--ink);
    position: relative;
  }

  /* ---------- Cover page ---------- */
  .cover {
    position: absolute;
    left: 10px; top: 15px;
    width: 575px; height: 970px;
    overflow: hidden;
  }
  .cover__backdrop {
    position: absolute; inset: 0;
    background:
      radial-gradient(ellipse at 40% 55%, rgba(120,20,30,0.55), transparent 60%),
      linear-gradient(180deg, var(--red-bright) 0%, var(--red) 45%, var(--red-deep) 100%);
  }
  .cover__band {
    position: absolute;
    left: 0; right: 0; top: 150px; height: 185px;
    background: var(--band);
    text-align: center;
    padding-top: 18px;
  }
  .cover__name {
    font-family: "Kaushan Script", cursive;
    color: var(--gold);
    font-size: 78px;
    line-height: 1;
    letter-spacing: 4px;
  }
  .cover__subtitle {
    font-family: "Kaushan Script", cursive;
    color: var(--gold);
    font-size: 46px;
    line-height: 1.3;
  }
  .cover__seal {
    position: absolute;
    left: 258px; top: 340px;
    width: 128px; height: 128px;
    border-radius: 50%;
    background: #fff;
  }

  /* ---------- Inside page ---------- */
  .inside {
    position: absolute;
    left: 600px; top: 15px;
    width: 590px; height: 970px;
    overflow: hidden;
    background: linear-gradient(180deg, var(--red-bright), var(--red) 50%, var(--red-deep));
  }
  .inside__sakura {
    position: absolute; inset: 0;
    background: radial-gradient(ellipse at 90% 30%, rgba(120,20,30,0.5), transparent 55%);
  }
  .dish-photos {
    position: absolute;
    left: 0; top: 0;
    width: 230px; height: 100%;
    display: flex; flex-direction: column; gap: 10px;
    padding: 0 0 10px 0;
  }
  .dish-photo {
    flex: 1;
    border-radius: 0 60px 60px 0;
    background: radial-gradient(circle at 45% 45%, #e9a06a 0%, #b5542c 45%, #7a1410 80%);
  }
  .dish-photo--prawn { background: radial-gradient(circle at 40% 40%, #f3b37a 0%, #d2692f 40%, #8a1612 80%); }
  .dish-photo--noodle { background: radial-gradient(circle at 45% 50%, #a8583a 0%, #6e2a1c 45%, #6a0f10 85%); }
  .dish-photo--veg { background: radial-gradient(circle at 45% 50%, #e2c49a 0%, #b96a4a 45%, #7a1410 85%); }

  .menu-panel {
    position: absolute;
    left: 230px; top: 58px;
    width: 335px; height: 890px;
    border: 8px solid var(--panel-yellow);
    background: linear-gradient(90deg, var(--panel-cream) 0%, var(--panel-cream) 55%, var(--panel-yellow) 100%);
    padding: 14px 14px 0 18px;
  }
  .menu-section + .menu-section { margin-top: 22px; }
  .menu-section__title {
    font-family: "Caveat", cursive;
    font-weight: 500;
    font-size: 36px;
    line-height: 1;
    margin-bottom: 6px;
  }
  .menu-list { list-style: none; padding-left: 8px; }
  .menu-item { margin-bottom: 6px; font-size: 11.5px; line-height: 13px; }
  .menu-item__name { font-weight: 600; }
  .menu-item__price { font-style: italic; font-weight: 400; }
  .menu-item__desc { display: block; font-style: italic; }
</style>
</head>
<body>

  <section class="cover">
    <div class="cover__backdrop" role="img" aria-label="Red background with dark cherry blossom branches"></div>
    <div class="cover__band">
      <div class="cover__name">MIRELO</div>
      <div class="cover__subtitle">Japanese Restaurant</div>
    </div>
    <div class="cover__seal"></div>
  </section>

  <section class="inside">
    <div class="inside__sakura" role="img" aria-label="Faint cherry blossom branches on red"></div>

    <div class="dish-photos">
      <div class="dish-photo" role="img" aria-label="Photo of a rice bowl topped with beef and egg"></div>
      <div class="dish-photo dish-photo--prawn" role="img" aria-label="Photo of a bowl with a tempura prawn"></div>
      <div class="dish-photo dish-photo--noodle" role="img" aria-label="Photo of a bowl of glazed meat and noodles"></div>
      <div class="dish-photo dish-photo--veg" role="img" aria-label="Photo of a bowl of stir-fried vegetables and noodles"></div>
    </div>

    <div class="menu-panel">
      <div class="menu-section">
        <h2 class="menu-section__title">Side dish</h2>
        <ul class="menu-list">
          <li class="menu-item"><span class="menu-item__name">Edamame</span> <span class="menu-item__price">$4</span><span class="menu-item__desc">Japanese Steam Green Bean</span></li>
          <li class="menu-item"><span class="menu-item__name">Crab Craw</span> <span class="menu-item__price">$3 each</span><span class="menu-item__desc">With Japanese mayo</span></li>
          <li class="menu-item"><span class="menu-item__name">Teriyaki Chicken Stick</span> <span class="menu-item__price">$3 each</span><span class="menu-item__desc">Chicken stick with home made teriyaki sauce</span></li>
          <li class="menu-item"><span class="menu-item__name">Tempura Prawns</span> <span class="menu-item__price">$7</span><span class="menu-item__desc">With Japanese mayo</span></li>
          <li class="menu-item"><span class="menu-item__name">Miso Soup</span> <span class="menu-item__price">$3</span><span class="menu-item__desc">Traditional Japanese soup</span></li>
          <li class="menu-item"><span class="menu-item__name">Salt and Pepper Calamari</span> <span class="menu-item__price">$7</span><span class="menu-item__desc">With japanese mayo</span></li>
        </ul>
      </div>

      <div class="menu-section">
        <h2 class="menu-section__title">Main dish</h2>
        <ul class="menu-list">
          <li class="menu-item"><span class="menu-item__name">Gyu Don</span> <span class="menu-item__price">$12</span><span class="menu-item__desc">Bowl of steam rice topped with beef and onion simmered in a mildly sweet sauce.</span></li>
          <li class="menu-item"><span class="menu-item__name">Teriyaki Don</span> <span class="menu-item__price">$12</span><span class="menu-item__desc">Bowl of steam rice topped with your choice of beef, chicken or pork and with our special Teriyaki sauce.</span></li>
          <li class="menu-item"><span class="menu-item__name">Vege Don</span> <span class="menu-item__price">$12</span><span class="menu-item__desc">Bowl of steam rice with seasonal vegetables with the special Japanese sweet soy sauce.</span></li>
          <li class="menu-item"><span class="menu-item__name">Japanese Curry</span> <span class="menu-item__price">$12,(prawns $14)</span><span class="menu-item__desc">Bowl of steam rice with chicken, pork or prawn with Japanese mild curry sauce.</span></li>
          <li class="menu-item"><span class="menu-item__name">Katsu Don</span> <span class="menu-item__price">$12</span><span class="menu-item__desc">Bowl of steam rice topped with a deep-fried pork cutlet and egg with the Japanese special sauce.</span></li>
          <li class="menu-item"><span class="menu-item__name">Oyako Don</span> <span class="menu-item__price">$12</span><span class="menu-item__desc">Bowl of steam rice topped with chick and egg with Japanese special sauce.</span></li>
          <li class="menu-item"><span class="menu-item__name">Spice Don</span> <span class="menu-item__price">$12</span><span class="menu-item__desc">Bowl of steam rice topped with beef or chicken with Japanese spice sauce.</span></li>
          <li class="menu-item"><span class="menu-item__name">Gingle Don</span> <span class="menu-item__price">$12</span><span class="menu-item__desc">Bowl of steam rice topped with beef or chicken with Japanese ginger sauce.</span></li>
          <li class="menu-item"><span class="menu-item__name">Sushi</span> <span class="menu-item__price">$3</span><span class="menu-item__desc">Roll everyday on seasonal ingredient.</span></li>
        </ul>
      </div>

      <div class="menu-section">
        <h2 class="menu-section__title">Japanese-style sweets</h2>
        <ul class="menu-list">
          <li class="menu-item" style="margin-bottom:2px"><span class="menu-item__name">Black Sesame Ice cream</span> <span class="menu-item__price">$4.5</span></li>
          <li class="menu-item"><span class="menu-item__name">Green Tea Ice cream</span> <span class="menu-item__price">$4.5</span></li>
        </ul>
      </div>
    </div>
  </section>

</body>
</html>
```